Computer Repair Business - Needs New Business Card Design

I want to create a very cool business card for my business. I want to make it 100% different from my previous card. I would like to use similar color scheme like Royal blue.

With this card I want to create a conversation and have my customers say "Wow, that's a cool business card" Trying to prevent it from looking like the typical card that get's shoved into a wallet.

My website is below:

www.milospcworks.com

I want to edit the hours and website and email:

www.milospcworks.com
milo@milospcworks.com

10:30 to 6pm Monday - Friday
10:30 to 3pm Saturday

Just to remind, when i see a new design i don't want to notice my old design.

Business card will be printed and made with rounded corners and horizontal.

The back of the card should say " In-Store Repair, Remote Support, Data Recovery"

Industry/Entity Type

Business

Font styles to use
Sans Serif

Colors
33a6d7
3176b5

Requirements
Must have
• Clean looking - have creative aspects.
Should not have
• Should not look like the previous card design.

```html
<!DOCTYPE html>
<html lang="en">
<head>
<meta charset="utf-8">
<title>Milo's PC Works Inc – Business Card</title>
<link rel="stylesheet" href="https://fonts.googleapis.com/css2?family=Raleway:wght@500;600;700&display=swap">
<style>
  :root {
    --canvas: #fffbf4;
    --card-front: #f0f1f5;
    --card-front-band: #e6e8ee;
    --royal: #0f55a0;
    --royal-band: #1b62ab;
    --ink-blue: #1a5a9e;
    --logo-ink: #2b2b2e;
    --white: #ffffff;
  }
  * { box-sizing: border-box; margin: 0; padding: 0; }
  html, body { width: 1200px; height: 1000px; overflow: hidden; }
  body {
    background: var(--canvas);
    font-family: "Raleway", Arial, sans-serif;
    position: relative;
  }
  .card {
    position: absolute;
    top: 346px;
    width: 544px;
    height: 307px;
    border-radius: 14px;
    overflow: hidden;
    box-shadow: 0 6px 14px rgba(0,0,0,0.12);
  }
  .card-front { left: 28px; background: var(--card-front); }
  .card-back { left: 596px; background: var(--royal); border-radius: 14px 14px 0 14px; }

  .band { position: absolute; display: block; }
  .card-front .band-upper { left: 100px; top: 138px; width: 460px; height: 50px; background: var(--card-front-band); border-radius: 24px 0 0 0; opacity: .7; }
  .card-front .band-lower { left: 86px; top: 200px; width: 470px; height: 46px; background: var(--card-front-band); opacity: .55; }
  .card-back .band-upper { left: 88px; top: 138px; width: 460px; height: 54px; background: var(--royal-band); border-radius: 26px 0 0 0; opacity: .55; }
  .card-back .band-lower { left: 84px; top: 200px; width: 470px; height: 110px; background: var(--royal-band); opacity: .45; }

  .brand-name {
    position: absolute;
    left: 30px;
    top: 30px;
    font-weight: 600;
    color: var(--logo-ink);
    font-size: 42px;
    letter-spacing: 1px;
    line-height: 1;
    display: flex;
    align-items: center;
    gap: 14px;
    white-space: nowrap;
  }
  .brand-name .brand-mark {
    width: 28px; height: 28px;
    background: var(--royal);
  }

  .contact-list {
    position: absolute;
    left: 30px;
    top: 154px;
    list-style: none;
    color: var(--ink-blue);
    font-size: 16.5px;
    font-weight: 500;
    line-height: 27px;
    white-space: nowrap;
  }
  .partner-badge {
    position: absolute;
    left: 370px;
    top: 266px;
    width: 150px;
    height: 16px;
    border-radius: 3px;
    background: var(--royal);
  }

  .service {
    position: absolute;
    top: 35px;
    width: 160px;
    text-align: center;
    color: var(--white);
    font-size: 14px;
    font-weight: 500;
    line-height: 17.5px;
  }
  .service-icon {
    display: block;
    width: 90px; height: 90px;
    margin: 0 auto 12px;
  }
  .service-instore { left: 12px; }
  .service-remote { left: 191px; }
  .service-recovery { left: 370px; }

  .hours {
    position: absolute;
    left: 0; right: 0;
    top: 232px;
    text-align: center;
    color: var(--white);
    font-size: 14px;
    font-weight: 700;
    line-height: 19px;
    white-space: nowrap;
  }
</style>
</head>
<body>

<section class="card card-front" aria-label="Business card front">
  <span class="band band-upper"></span>
  <span class="band band-lower"></span>
  <h1 class="brand-name"><span>MILO'S PC WORKS</span><span class="brand-mark"></span></h1>
  <ul class="contact-list">
    <li>Computer Repair&nbsp; / &nbsp;Sales</li>
    <li>512 Ridge Road, Fairview, NJ 07022</li>
    <li>555.314.2718</li>
    <li>milo@milospcworks.com</li>
    <li>www.milospcworks.com</li>
  </ul>
  <span class="partner-badge" aria-label="Partner badge"></span>
</section>

<section class="card card-back" aria-label="Business card back">
  <span class="band band-upper"></span>
  <span class="band band-lower"></span>

  <div class="service service-instore">
    <svg class="service-icon" viewBox="0 0 90 90" aria-hidden="true">
      <circle cx="45" cy="45" r="45" fill="#fff"/>
      <g transform="rotate(-45 45 45)" fill="#0f55a0">
        <rect x="39" y="8" width="12" height="30" rx="5"/>
        <rect x="37" y="36" width="16" height="5" rx="2"/>
        <rect x="43" y="41" width="4" height="34"/>
        <rect x="40" y="74" width="10" height="6" rx="1"/>
      </g>
    </svg>
    In-Store<br>Repair
  </div>

  <div class="service service-remote">
    <svg class="service-icon" viewBox="0 0 90 90" aria-hidden="true">
      <circle cx="45" cy="45" r="45" fill="#fff"/>
      <g fill="none" stroke="#0f55a0" stroke-width="3">
        <circle cx="45" cy="45" r="32"/>
        <ellipse cx="45" cy="45" rx="14" ry="32"/>
        <line x1="45" y1="13" x2="45" y2="77"/>
        <line x1="13" y1="45" x2="77" y2="45"/>
        <path d="M18 29 H72 M18 61 H72"/>
      </g>
    </svg>
    Remote<br>Support
  </div>

  <div class="service service-recovery">
    <svg class="service-icon" viewBox="0 0 90 90" aria-hidden="true">
      <circle cx="45" cy="45" r="45" fill="#fff"/>
      <g transform="rotate(-45 45 45)" fill="#0f55a0">
        <rect x="24" y="24" width="42" height="42" rx="3"/>
        <g>
          <rect x="28" y="16" width="4" height="7"/><rect x="36" y="16" width="4" height="7"/><rect x="44" y="16" width="4" height="7"/><rect x="52" y="16" width="4" height="7"/><rect x="60" y="16" width="4" height="7"/>
          <rect x="28" y="67" width="4" height="7"/><rect x="36" y="67" width="4" height="7"/><rect x="44" y="67" width="4" height="7"/><rect x="52" y="67" width="4" height="7"/><rect x="60" y="67" width="4" height="7"/>
          <rect x="16" y="28" width="7" height="4"/><rect x="16" y="36" width="7" height="4"/><rect x="16" y="44" width="7" height="4"/><rect x="16" y="52" width="7" height="4"/><rect x="16" y="60" width="7" height="4"/>
          <rect x="67" y="28" width="7" height="4"/><rect x="67" y="36" width="7" height="4"/><rect x="67" y="44" width="7" height="4"/><rect x="67" y="52" width="7" height="4"/><rect x="67" y="60" width="7" height="4"/>
        </g>
        <rect x="34" y="34" width="22" height="22" fill="#fff"/>
      </g>
    </svg>
    Data<br>Recovery
  </div>

  <p class="hours">
    Hours&nbsp; / &nbsp;MON - FRI 10:30 am - 6:00 pm&nbsp; / &nbsp;SAT 10:30 am - 3:00 pm<br>
    After hours support available by appointment
  </p>
</section>

</body>
</html>
```